43 Year Old Construction firm needs Updated Business Card & Stationery Design

We are an established and well known (in our market) commercial construction firm. We need a cleaner and more modern look for our corporate identity material. We would like to continue to use our current colors and logo.
We are thinking about incorporating a slogan on our business card (either front or back): "Striving to be the most trusted builder in our market." The text could change at some point. Our website is www.kvoplarn.com . Sample card is attached. Some will have more phone numbers, etc...
Updates

Target Market(s)

Commercial and institutional clients.

Industry/Entity Type

Construction Company

Contact Information for Business Card

See attached for existing card. But don't be constrained.

Requirements
Must have
• Logo, name, title, address, website, email, phone numbers (as few as one, as many as three)
• Slogan on front or back "Striving to be the most trusted builder in our market"
• Use existing logo and colors

```html
<!DOCTYPE html>
<html lang="en">
<head>
<meta charset="utf-8">
<title>Kvoplarn Business Card</title>
<link href="https://fonts.googleapis.com/css2?family=Open+Sans:wght@400;600;700&display=swap" rel="stylesheet">
<style>
  :root {
    --backdrop: #cbcbcb;
    --navy: #0e4781;
    --navy-faint: #3a6c9f;
    --green: #1fa34c;
    --white: #ffffff;
    --slogan: #c9d8ea;
    --card-shadow: 4px 6px 10px rgba(0,0,0,0.28);
  }
  html, body {
    margin: 0;
    padding: 0;
    width: 1200px;
    height: 861px;
    overflow: hidden;
    background: var(--backdrop);
    font-family: "Open Sans", Arial, sans-serif;
  }
  .stage { position: relative; width: 1200px; height: 861px; }

  .card {
    position: absolute;
    left: 307px;
    width: 573px;
    height: 322px;
    box-shadow: var(--card-shadow);
    overflow: hidden;
  }

  /* Front */
  .card-front { top: 80px; background: var(--navy); }
  .front-white {
    position: absolute; left: 0; top: 0; width: 228px; height: 100%;
    background: var(--white);
    box-sizing: border-box; border: 1px solid #444; border-right: none;
  }
  .company-name {
    position: absolute; left: 33px; top: 38px; margin: 0;
    font-weight: 700; font-size: 28px; line-height: 1; letter-spacing: 1px;
    color: var(--navy);
  }
  .accent-line {
    position: absolute; left: 33px; top: 92px; width: 514px; height: 6px;
    background: var(--green);
  }
  .direct-line {
    position: absolute; left: 45px; top: 289px; margin: 0;
    font-size: 13px; line-height: 18px; color: var(--navy);
  }
  .person-name {
    position: absolute; right: 27px; top: 55px; margin: 0;
    font-size: 21px; line-height: 28px; font-weight: 400; color: var(--white); white-space: nowrap;
  }
  .person-title {
    position: absolute; left: 389px; top: 105px; margin: 0;
    font-size: 16px; line-height: 22px; letter-spacing: 1.5px; color: var(--white); white-space: nowrap;
  }
  .contact-list {
    position: absolute; right: 26px; top: 189px; margin: 0; padding: 0; list-style: none;
  }
  .contact-list li {
    display: flex; justify-content: flex-end; align-items: center;
    height: 21.4px; font-size: 16px; letter-spacing: 1.6px; color: var(--white); white-space: nowrap;
  }
  .contact-list svg { width: 14px; height: 14px; margin-left: 18px; fill: var(--green); flex: none; }

  /* Back */
  .card-back { top: 455px; background: var(--navy); }
  .back-name {
    position: absolute; left: 0; right: 0; top: 90px; margin: 0; text-align: center;
    font-weight: 700; font-size: 88px; line-height: 1; letter-spacing: 2px; color: var(--navy-faint);
  }
  .slogan {
    position: absolute; left: 0; right: 0; top: 236px; margin: 0; text-align: center;
    font-size: 14px; line-height: 20px; letter-spacing: 0.5px; color: var(--slogan);
  }
  .back-rule {
    position: absolute; top: 289px; height: 6px; background: var(--green);
  }
  .back-rule.left { left: 0; width: 218px; }
  .back-rule.right { right: 0; width: 219px; }
  .website {
    position: absolute; left: 0; right: 0; top: 282px; margin: 0; text-align: center;
    font-size: 14px; line-height: 20px; color: var(--green);
  }
</style>
</head>
<body>
<main class="stage">
  <section class="card card-front">
    <div class="front-white">
      <p class="company-name">KVOPLARN</p>
      <p class="direct-line">Direct 555-333-0162</p>
    </div>
    <div class="accent-line"></div>
    <p class="person-name">Marcus T. Elvendale</p>
    <p class="person-title">President</p>
    <ul class="contact-list">
      <li>555-410-2690
        <svg viewBox="0 0 14 14" aria-hidden="true"><path d="M4 0h6a1 1 0 0 1 1 1v12a1 1 0 0 1-1 1H4a1 1 0 0 1-1-1V1a1 1 0 0 1 1-1zm.5 1.5v9h5v-9z"/></svg></li>
      <li>555-781-0182
        <svg viewBox="0 0 14 14" aria-hidden="true"><path d="M1 5c0-2 3-3 6-3s6 1 6 3v1h-3V5H4v1H1zm2 2h8l1 6H2z"/></svg></li>
      <li>555-781-0354
        <svg viewBox="0 0 14 14" aria-hidden="true"><path d="M3 1h8v4h2v8H1V5h2zm1 1v3h6V2zM3 8v3h8V8z"/></svg></li>
      <li>marcuse@kvoplarn.com
        <svg viewBox="0 0 14 14" aria-hidden="true"><path d="M1 3h12v8H1z"/></svg></li>
      <li>4210 Harwell Ave. Brookton
        <svg viewBox="0 0 14 14" aria-hidden="true"><path d="M7 0a5 5 0 0 1 5 5c0 4-5 9-5 9S2 9 2 5a5 5 0 0 1 5-5zm0 3a2 2 0 1 0 0 4 2 2 0 0 0 0-4z"/></svg></li>
    </ul>
  </section>

  <section class="card card-back">
    <p class="back-name">KVOPLARN</p>
    <p class="slogan">Striving to be the most trusted builder in our market.</p>
    <div class="back-rule left"></div>
    <p class="website">www.kvoplarn.com</p>
    <div class="back-rule right"></div>
  </section>
</main>
</body>
</html>
```